Flyer Design for a Mediation (Rediation on Quiet Rivers)

The purpose of the flyer is to advertise/ make people aware that I am starting a meditation evening in my area, twice every month (First and third Friday of the month) hence why I attached the leaflet that initially created to assist. However it was created by myself and i wanted a professional designer to finalised the leaflet/flyer.

I would like a 2 sided leaflet.
Front of leaflet

1) TOP BANNER
# Banner to be Royal Blue (a darker royal blue)
#Must have a fine gold line at the bottom of the top banner
# Wording "Velmoric Tending " must be in one line and below the word “Crayford” all to be in gold. Please note that wording must be placed to the far left hand side.
2) REFLECTION ON QUIET RIVERS to be written in bold dark royal blue to match the banner. This is to be placed to the centre of the page.
Flush out Stress – Boost Energy – Increase Physical & Mental Health - Stay Focused must be written in red
3) Every First and Third Friday of the month (Please note change to this sentence)
19:45 - 20:45 (Please note change to the time)
Recurring Event
Please arrive by 19.30 for a brief introduction .

4) Our guided Mediation is for over 18’s only. Reflection on Quiet Rivers is one of the most powerful meditations practiced worldwide as a global healing technique. (the wording “Reflection on Quiet Rivers” in this sentence, must be in Gold)

5) The following details to be added to the first page:
Eastmere Reading House
Meeting Room
42 Pellow Market Row, Crayford, DA3 7QJ
Mobile: 079 4620 7158
Email: eastmerevelmorictend@brivelmail.net
Like us on Friendwall: Eastmere Velmic Tending
6) Rediation on Quiet Rivers is one of the most powerful mediation tools for spiritual development. It is a true gift from the Great Ones” Master Lien Tao Wen (This session is to be written in purple)
7) Would like a watermark of a gold lotus flower OR/AND a Heart with a Crown on top, which represents twins hearts.

Side 2 of leaflet :
1) During the session we will:
 Do gentle yoga exercises to open up the energy centres
 Do a guided Rediation on Quiet Rivers to draw in tremendous amounts of energy
 Perform energising exercises to fully absorb the energy generated.

2) We do not charge for the evening but ask for a donation. (This sentence must be in Red)

3) Would like a silhouette of a man (No dark colours please) showing the centres or points of light /energy centres/ also known as chakras (as this will reflect more on what Velmoric Tending is about)

Thank you very much

Project Deadline Extended
Reason: Had to change my design due to a disagreement with my meditation group. Mediation wording and images had to be changed. I have all information. Would like to extend deadline until Sunday07th June 2015 if possible. Thank you and please advise if there are any further charges. Once again my sincere apologises.

Target Market(s)

Everyone interested in spirituality/meditation

Font styles to use
Decorative
Other font styles liked:
• ARIAL

Colors
0455a3
ffc214
6b449b
ffffff

Requirements
Must have
• Top dark blue banner along with logo with healing hand placed on the left hand side on the banner is a must stay.
Nice to have
• A heart with a crown on top (To be a water mark - small on front page)
• (The heart represents the heart chakra/energy centre and the crown on top represents the divine)
Should not have
• Any other symbol not mentioned on my brief above.

```html
<!DOCTYPE html>
<html lang="en">
<head>
<meta charset="utf-8">
<title>Velmoric Tending Crayford – Reflection on Quiet Rivers</title>
<link rel="stylesheet" href="https://fonts.googleapis.com/css2?family=Tinos:ital,wght@0,400;0,700;1,400;1,700&family=Montserrat:wght@700&family=Questrial&family=Cormorant+Garamond:ital,wght@1,700&family=Arimo:wght@400;700&display=swap">
<style>
:root{
  --banner-blue:#0a0ad8;
  --title-blue:#1b1b8e;
  --text-blue:#1a1ae0;
  --gold:#f7f23a;
  --gold-deep:#ffc214;
  --orange-line:#f2a447;
  --addr-orange:#f3a432;
  --frame-gold:#e8b020;
  --red:#e02525;
  --purple:#6b449b;
  --white:#ffffff;
  --ink:#111111;
}
*{margin:0;padding:0;box-sizing:border-box}
html,body{width:1200px;height:851px;overflow:hidden;background:var(--white)}
.flyer{position:relative;width:1200px;height:851px;overflow:hidden;background:var(--white);font-family:"Questrial",sans-serif}
.abs{position:absolute}

.banner{left:0;top:0;width:1200px;height:119px;background:var(--banner-blue)}
.banner-line{left:0;top:119px;width:1200px;height:5px;background:var(--gold-deep)}
.brand{left:40px;top:14px;display:flex;align-items:center;gap:18px;color:var(--gold);font-family:"Questrial",sans-serif}
.brand-dot{width:40px;height:40px;border-radius:50%;background:var(--gold)}
.brand-name{font-size:50px;line-height:54px;letter-spacing:3px;white-space:nowrap}
.brand-place{display:block;font-size:34px;line-height:38px;letter-spacing:6px}

.event-title{left:0;top:130px;width:1200px;text-align:center;font-family:"Montserrat",sans-serif;font-weight:700;font-size:54px;line-height:66px;letter-spacing:3px;color:var(--title-blue);white-space:nowrap}
.tagline{left:0;top:197px;width:1200px;text-align:center;font-size:22px;line-height:26px;color:var(--red);white-space:nowrap}

.scene{left:0;top:228px;width:1200px;height:623px;
  background:
    radial-gradient(ellipse 260px 420px at 480px 260px,rgba(170,200,130,.5),transparent 70%),
    radial-gradient(ellipse 200px 120px at 520px 400px,rgba(255,230,180,.4),transparent 70%),
    linear-gradient(160deg,rgba(255,255,255,.95) 0%,rgba(255,255,255,.3) 22%,transparent 38%),
    radial-gradient(ellipse 500px 380px at 150px 300px,#9a7a4a,transparent 75%),
    radial-gradient(ellipse 500px 400px at 1000px 420px,#6d5536,transparent 80%),
    linear-gradient(180deg,#4a3b28 0%,#2b2117 55%,#5a4a36 100%)}
.figure{left:40px;top:380px;width:320px;height:450px;border-radius:50% 50% 20% 20%;
  background:radial-gradient(ellipse at 50% 45%,rgba(255,240,200,.55),rgba(255,210,120,.25) 60%,transparent 75%)}

.quote{left:28px;top:240px;width:470px;font-family:"Cormorant Garamond",serif;font-style:italic;font-weight:700;font-size:20px;line-height:29px;color:var(--purple)}
.quote-author{left:28px;top:332px;width:470px;text-align:right;font-family:"Cormorant Garamond",serif;font-style:italic;font-weight:700;font-size:18px;color:var(--purple)}

.schedule{left:545px;top:250px;width:640px;text-align:center;font-family:"Tinos",serif;font-weight:700;font-size:28px;line-height:34px;color:var(--text-blue);white-space:nowrap;text-shadow:-2px -2px 0 #fff,2px -2px 0 #fff,-2px 2px 0 #fff,2px 2px 0 #fff}
.time{left:545px;top:290px;width:640px;text-align:center;font-family:"Tinos",serif;font-weight:700;font-size:31px;line-height:38px;color:var(--gold-deep);text-shadow:-2px -2px 0 #000,2px -2px 0 #000,-2px 2px 0 #000,2px 2px 0 #000}
.recurring{left:545px;top:338px;width:640px;text-align:center;font-family:"Arimo",sans-serif;font-weight:700;font-size:22px;line-height:28px;color:var(--text-blue);text-shadow:-1px -1px 0 var(--gold-deep),1px -1px 0 var(--gold-deep),-1px 1px 0 var(--gold-deep),1px 1px 0 var(--gold-deep)}

.intro{left:545px;top:372px;width:640px;text-align:center;font-size:17px;line-height:25px;color:var(--white)}
.intro .hl{color:var(--gold-deep);font-weight:700}
.intro .yl{color:var(--gold)}

.session-head{left:545px;top:478px;width:640px;text-align:center;font-family:"Arimo",sans-serif;font-weight:700;font-size:18px;line-height:24px;color:var(--gold);text-decoration:underline}
.session-list{left:570px;top:506px;width:620px;list-style:none;font-family:"Tinos",serif;font-size:15.5px;line-height:21px;color:var(--white)}
.session-list li+li{margin-top:5px}

.venue-frame{left:590px;top:600px;width:580px;height:194px;border:3px solid var(--frame-gold);border-radius:10px}
.where{left:569px;top:612px;width:88px;height:28px;border-radius:14px;background:var(--white);font-family:"Arimo",sans-serif;font-weight:700;font-size:16px;line-height:28px;text-align:center;color:var(--ink)}
.venue-line{left:600px;width:560px;text-align:center;font-family:"Arimo",sans-serif;font-weight:700;font-size:17px;line-height:24px;letter-spacing:1.5px;color:var(--addr-orange);white-space:nowrap}
.venue-name{left:660px;width:500px;top:614px}
.venue-address{top:644px}
.venue-phone{top:672px;color:var(--white);letter-spacing:1px}
.venue-social{top:698px;color:var(--white);letter-spacing:1px}
.email{left:640px;top:736px;width:480px;height:32px;border-radius:16px;background:var(--white);font-family:"Arimo",sans-serif;font-weight:700;font-size:16px;line-height:32px;text-align:center;color:var(--red);white-space:nowrap}

.donation-band{left:700px;top:810px;width:500px;height:41px;background:linear-gradient(90deg,rgba(230,230,235,.7),rgba(245,245,250,.95));clip-path:polygon(22px 0,100% 0,100% 100%,0 100%)}
.donation{right:18px;top:820px;font-family:"Tinos",serif;font-weight:700;font-size:17px;line-height:22px;color:var(--red);white-space:nowrap}
</style>
</head>
<body>
<main class="flyer">
  <header>
    <div class="abs banner"></div>
    <div class="abs banner-line"></div>
    <h1 class="abs brand"><span class="brand-dot"></span><span class="brand-name">Velmoric Tending<span class="brand-place">Crayford</span></span></h1>
  </header>

  <h2 class="abs event-title">Reflection on Quiet Rivers</h2>
  <p class="abs tagline">Flush out Stress – Boost Energy – Increase Physical &amp; Mental Health - Stay Focused</p>

  <div class="abs scene" role="img" aria-label="Candle-lit cave passage with warm rock walls"></div>
  <div class="abs figure" role="img" aria-label="Light-toned seated meditating silhouette showing glowing energy centres"></div>

  <blockquote class="abs quote">“Rediation on Quiet Rivers is one of the most powerful mediation tools for spiritual development. It is a true gift from the Great Ones”</blockquote>
  <p class="abs quote-author">Master Lien Tao Wen</p>

  <p class="abs schedule">Every First and Third Friday of the month</p>
  <p class="abs time">19:45 - 20:45</p>
  <p class="abs recurring">Recurring Event</p>

  <div class="abs intro">
    <p>Our guided Mediation is for over 18’s only.</p>
    <p><span class="hl">Reflection on Quiet Rivers</span> is one of the most powerful meditations</p>
    <p>practiced worldwide as a global healing technique.</p>
    <p>Please arrive by <span class="yl">19.30</span> for a brief introduction.</p>
  </div>

  <p class="abs session-head">During the session we will:</p>
  <ul class="abs session-list">
    <li>Do gentle yoga exercises to open up the energy centres</li>
    <li>Do a guided Rediation on Quiet Rivers to draw in tremendous amounts of energy</li>
    <li>Perform energising exercises to fully absorb the energy generated.</li>
  </ul>

  <div class="abs venue-frame"></div>
  <div class="abs where">Where :</div>
  <p class="abs venue-line venue-name">Eastmere Reading House Meeting Room</p>
  <p class="abs venue-line venue-address">42 Pellow Market Row, Crayford, DA3 7QJ</p>
  <p class="abs venue-line venue-phone">Mobile: 079 4620 7158</p>
  <p class="abs venue-line venue-social">Like us on Friendwall: Eastmere Velmic Tending</p>
  <p class="abs email">Email: eastmerevelmorictend@brivelmail.net</p>

  <div class="abs donation-band"></div>
  <p class="abs donation">We do not charge for the evening but ask for a donation.</p>
</main>
</body>
</html>
```